Bully breed rescue website

I need a website for my bully breed rescue. We rescue bully breeds from up and down the east coast of the United States and train them as service dogs for people with limited mobility disabilities. I don't want a lot of white space. I want it to be modern and slick and colorful and still look professional. I want it to be different and have a lot of wow factor. I linked a copy of my logo.

Number of Pages Required

5+ page

Font styles to use
Sans Serif

Colors

Designer to choose colors to be used in the design.

Requirements
Must have
• Moving aspects. Blog and ecommerce.
• 1.) Home page
• 2.) Services- something modular
• 3.) About US
• 4.) Blog
• 5.) Application page
• 6.) Donation page
• 7.) Contact Us
Nice to have
• Large Slider of photos on home page
• vertical menu bar
Should not have
• Lots of white space. Dont want it to look like a template or any other site

```html
<!DOCTYPE html>
<html lang="en">
<head>
<meta charset="UTF-8">
<title>Gentle Paws Rescue — Home</title>
<link rel="stylesheet" href="https://fonts.googleapis.com/css2?family=Lato:ital,wght@0,400;0,700;0,900;1,400;1,700&display=swap">
<style>
  :root {
    --ink: #1b1b1b;
    --nav-black: #111111;
    --page: #f4f5f6;
    --white: #ffffff;
    --red: #e8262f;
    --yellow: #f7cf0a;
    --muted: #8a8d91;
    --text: #4a4d52;
    --hero-a: #6f7a4a;
    --hero-b: #3c3a2a;
    --hero-c: #b79a6a;
  }
  * { box-sizing: border-box; margin: 0; padding: 0; }
  html, body { width: 1200px; height: 900px; overflow: hidden; }
  body {
    background: var(--page);
    font-family: "Lato", sans-serif;
    color: var(--ink);
    position: relative;
  }

  /* Header */
  .site-header { position: absolute; top: 0; left: 0; width: 1200px; height: 82px; background: var(--white); }
  .call-us { position: absolute; left: 70px; top: 18px; font-size: 15px; color: var(--ink); display: flex; align-items: center; gap: 6px; }
  .call-us .label { color: var(--red); font-style: italic; font-weight: 700; }
  .donate-btn {
    position: absolute; right: 60px; top: 12px; height: 28px; padding: 0 22px;
    background: var(--red); color: var(--white); border-radius: 14px;
    font-size: 11px; font-weight: 700; text-transform: uppercase; letter-spacing: .5px;
    display: flex; align-items: center;
  }
  .main-nav { position: absolute; top: 50px; height: 30px; background: var(--nav-black); display: flex; align-items: center; }
  .main-nav.left { left: 60px; width: 430px; padding-left: 20px; }
  .main-nav.right { right: 60px; width: 430px; justify-content: flex-end; padding-right: 24px; }
  .main-nav a {
    color: var(--white); font-size: 11px; text-transform: uppercase; letter-spacing: .6px;
    text-decoration: none; padding: 0 18px; border-right: 1px solid #444; line-height: 12px;
  }
  .main-nav a:last-child { border-right: none; }
  .main-nav a.active { color: var(--yellow); border-bottom: 2px solid var(--yellow); padding-bottom: 6px; margin-top: 8px; }

  .brand {
    position: absolute; left: 520px; top: 6px; width: 160px; height: 160px; border-radius: 50%;
    background: var(--white); z-index: 3; display: flex; align-items: center; justify-content: center;
    text-align: center; font-weight: 900; font-size: 22px; line-height: 1.05; color: var(--ink); padding: 0 18px;
  }

  /* Hero */
  .hero {
    position: absolute; top: 80px; left: 0; width: 1200px; height: 400px;
    background: linear-gradient(100deg, var(--hero-c) 0%, var(--hero-a) 35%, var(--hero-b) 75%, #2a2a22 100%);
  }
  .hero-content { position: absolute; left: 360px; top: 150px; width: 520px; text-align: center; color: var(--white); }
  .hero-title { font-size: 44px; font-style: italic; font-weight: 400; margin-bottom: 14px; }
  .hero-text { font-size: 15px; font-style: italic; line-height: 1.45; margin-bottom: 18px; }
  .hero-cta {
    display: inline-block; background: var(--yellow); color: var(--ink); font-size: 10px; font-weight: 700;
    text-transform: uppercase; padding: 8px 18px; border-radius: 14px;
  }
  .slider-arrow { position: absolute; top: 200px; width: 30px; height: 30px; border-radius: 50%; display: flex; align-items: center; justify-content: center; }
  .slider-arrow.prev { left: 60px; background: rgba(255,255,255,.55); }
  .slider-arrow.next { right: 60px; background: var(--yellow); }

  /* Services */
  .services { position: absolute; top: 480px; left: 0; width: 1200px; height: 220px; text-align: center; }
  .eyebrow { font-size: 10px; letter-spacing: 1px; text-transform: uppercase; color: var(--muted); padding-top: 18px; }
  .section-title { font-size: 26px; font-weight: 700; margin-top: 4px; }
  .section-title .accent { color: var(--red); }
  .service-row { position: absolute; left: 150px; top: 78px; width: 900px; height: 132px; display: flex; gap: 6px; }
  .service-card { position: relative; flex: 1; overflow: hidden; }
  .service-card .photo { position: absolute; inset: 0; }
  .service-card .name {
    position: absolute; left: 0; right: 0; bottom: 8px; color: var(--white); font-size: 13px; font-weight: 700;
  }
  .service-card .overlay {
    position: absolute; inset: 0; background: rgba(0,0,0,.55); color: var(--white); padding: 14px 30px;
  }
  .overlay h3 { font-size: 14px; font-weight: 700; margin-bottom: 6px; }
  .overlay p { font-size: 10px; line-height: 1.35; margin-bottom: 8px; }
  .overlay .learn { display: inline-block; background: var(--yellow); color: var(--ink); font-size: 9px; font-weight: 700; text-transform: uppercase; padding: 4px 12px; border-radius: 10px; }
  .photo.training { background: linear-gradient(135deg, #6a7358, #2e3226); }
  .photo.adopt { background: linear-gradient(135deg, #8a8f7a, #3d4233); }
  .photo.foster { background: linear-gradient(135deg, #7f8a5c, #4a5236); }
  .photo.shelter { background: linear-gradient(135deg, #93a05e, #c4883f); }

  /* About */
  .about { position: absolute; top: 700px; left: 0; width: 1200px; height: 160px; text-align: center; }
  .about .eyebrow { padding-top: 10px; }
  .about-text { width: 520px; margin: 10px auto 10px; font-size: 11px; line-height: 1.5; color: var(--text); }
  .discover { font-size: 10px; text-transform: uppercase; letter-spacing: .6px; color: var(--ink); display: inline-flex; align-items: center; gap: 6px; }
  .discover::before { content: ""; width: 6px; height: 6px; border-radius: 50%; background: var(--ink); }
  .about-art { position: absolute; top: 20px; width: 130px; height: 120px; border-radius: 6px; }
  .about-art.left { left: 170px; background: linear-gradient(135deg, #ffffff, #d9d9d9); border: 1px solid #e2e2e2; }
  .about-art.right { right: 170px; background: linear-gradient(135deg, #f3e6d6, #a85a2a); }

  .gallery-strip { position: absolute; top: 866px; left: 150px; width: 900px; height: 34px; background: linear-gradient(90deg, #5a4a3a, #8a7a62, #4a4036); }
</style>
</head>
<body>
  <header class="site-header">
    <div class="call-us">
      <span class="label">Call Us:</span>
      <svg width="14" height="14" viewBox="0 0 24 24" aria-hidden="true"><path fill="#e8262f" d="M6.6 10.8a15.1 15.1 0 0 0 6.6 6.6l2.2-2.2c.3-.3.7-.4 1-.2 1.1.4 2.3.6 3.6.6.6 0 1 .4 1 1V20c0 .6-.4 1-1 1A17 17 0 0 1 3 4c0-.6.4-1 1-1h3.5c.6 0 1 .4 1 1 0 1.3.2 2.5.6 3.6.1.3 0 .7-.2 1z"/></svg>
      <span>123-456-7890</span>
    </div>
    <a class="donate-btn">Donation Now!</a>
    <nav class="main-nav left">
      <a class="active">Home</a><a>About Us</a><a>Services</a>
    </nav>
    <nav class="main-nav right">
      <a>Blog</a><a>Application</a><a>Contact Us</a>
    </nav>
  </header>

  <div class="brand">Gentle Paws Rescue</div>

  <section class="hero" role="img" aria-label="Photo of a young woman hugging a large rescue dog outdoors">
    <div class="hero-content">
      <h1 class="hero-title">We take care of your dog</h1>
      <p class="hero-text">We rescue bully breeds from up and down the east coast of the United States and train them as service dogs for people with limited mobility disabilities</p>
      <span class="hero-cta">Explore More</span>
    </div>
    <span class="slider-arrow prev"><svg width="10" height="10" viewBox="0 0 10 10"><path d="M6.5 1.5 3 5l3.5 3.5" stroke="#333" stroke-width="1.6" fill="none"/></svg></span>
    <span class="slider-arrow next"><svg width="10" height="10" viewBox="0 0 10 10"><path d="M3.5 1.5 7 5 3.5 8.5" stroke="#111" stroke-width="1.6" fill="none"/></svg></span>
  </section>

  <section class="services">
    <p class="eyebrow">What we do</p>
    <h2 class="section-title">Quality <span class="accent">Services</span></h2>
    <div class="service-row">
      <article class="service-card">
        <div class="photo training" role="img" aria-label="Photo of several dogs in obedience training"></div>
        <span class="name">Dog Training</span>
      </article>
      <article class="service-card">
        <div class="photo adopt" role="img" aria-label="Photo of a dog waiting for adoption"></div>
        <div class="overlay">
          <h3>Dog Adopt</h3>
          <p>Every rescue gets patient care, training and a careful match with a loving new home.</p>
          <span class="learn">Learn More</span>
        </div>
      </article>
      <article class="service-card">
        <div class="photo foster" role="img" aria-label="Photo of a foster volunteer with a dog"></div>
        <span class="name">Foster Care</span>
      </article>
      <article class="service-card">
        <div class="photo shelter" role="img" aria-label="Photo of a dog running on grass at the shelter"></div>
        <span class="name">Accepting Shelter</span>
      </article>
    </div>
  </section>

  <section class="about">
    <div class="about-art left" role="img" aria-label="Illustration of a spotted dog"></div>
    <div class="about-art right" role="img" aria-label="Illustration of a large brown and white dog"></div>
    <p class="eyebrow">Discover</p>
    <h2 class="section-title">About <span class="accent">Us</span></h2>
    <p class="about-text">We are a volunteer team giving bully breeds a second chance. Each dog is rescued, cared for and trained to support people with limited mobility, building trust and independence together every single day.</p>
    <span class="discover">Discover More</span>
  </section>

  <div class="gallery-strip" role="img" aria-label="Row of photos of rescued dogs"></div>
</body>
</html>
```